Life Coach for Lawyers Business Card Design

Elegant, original, business card design for life coaching service for associate attorneys who work in big law and struggle with stress, overwhelm, and time management. Double sided design.

Target Market(s)

Women associate attorneys who work in big law and struggle with stress, overwhelm, and time management.

Industry/Entity Type

Life Coaching

Contact Information for Business Card

Marissa Pendrell
Life Coach
518.677.3941
calmbriefcounsel.net
marissa@calmbriefcounsel.net
@calmbriefcounsel (Instagram)

Font styles to use
Other font styles liked:
• Silver South font duo. See uploaded files.

Requirements
Must have
• Icons for phone, website, email, and Instagram instead of words. Specific colors used in my logo (171B2B, 421121, FFFFFF)
Nice to have
• Foil. Embossed. Feminine design.
Should not have
• Any colors other than those used in logo. See uploaded files.

```html
<!DOCTYPE html>
<html lang="en">
<head>
<meta charset="utf-8">
<title>Calm Brief Counsel — Business Card</title>
<link rel="stylesheet" href="https://fonts.googleapis.com/css2?family=Cinzel:wght@500;700&family=Lato:wght@400;700&display=swap">
<style>
  :root {
    --navy: #171B2B;
    --wine: #421121;
    --white: #FFFFFF;
    --ink: #2a1a22;
    --card: #eef1f4;
    --stage: #c9d3dd;
    --rule: #4a4a52;
    --band-text: #e8d6dc;
  }
  * { margin: 0; padding: 0; box-sizing: border-box; }
  html, body {
    width: 1200px; height: 831px; overflow: hidden;
    background: var(--stage);
  }
  .card {
    position: absolute; left: 100px; top: 131px;
    width: 1000px; height: 568px;
    background: var(--card);
    color: var(--ink);
    overflow: hidden;
  }
  .brand {
    position: absolute; right: 44px; top: 92px;
    font-family: "Cinzel", serif; font-weight: 500;
    font-size: 46px; line-height: 1.05; text-align: right;
    letter-spacing: 1px; color: var(--wine);
  }
  .name {
    position: absolute; left: 44px; top: 298px;
    font-family: "Cinzel", serif; font-weight: 700;
    font-size: 34px; line-height: 42px; letter-spacing: 1px; color: var(--wine);
  }
  .name-rule {
    position: absolute; left: 44px; top: 344px;
    width: 912px; height: 3px; background: var(--navy);
  }
  .role {
    position: absolute; left: 44px; top: 358px;
    font-family: "Cinzel", serif; font-weight: 500;
    font-size: 23px; line-height: 30px; letter-spacing: 3px; color: var(--ink);
  }
  .contacts { position: absolute; left: 44px; top: 410px; list-style: none; }
  .contacts li {
    display: flex; align-items: center; gap: 22px;
    height: 34px;
    font-family: "Lato", sans-serif; font-weight: 700;
    font-size: 23px; letter-spacing: 1px; color: var(--navy);
  }
  .contacts svg { width: 26px; height: 26px; fill: var(--navy); flex: none; }
  .handle-mark {
    width: 20px; height: 20px; margin: 0 3px;
    border-radius: 50%; background: var(--navy); flex: none;
  }
  .footer { position: absolute; left: 0; bottom: 0; width: 1000px; height: 60px; }
  .site {
    position: absolute; right: 36px; bottom: 14px;
    display: flex; align-items: center; gap: 12px;
    font-family: "Lato", sans-serif; font-weight: 400;
    font-size: 22px; line-height: 28px; letter-spacing: 1.5px; color: var(--band-text);
  }
  .site svg { width: 22px; height: 22px; fill: none; stroke: var(--band-text); stroke-width: 1.6; }
</style>
</head>
<body>
  <main class="card">
    <div class="brand">Calm Brief<br>Counsel</div>

    <h1 class="name">Marissa Pendrell</h1>
    <div class="name-rule"></div>
    <p class="role">LIFE COACH</p>

    <ul class="contacts">
      <li>
        <svg viewBox="0 0 24 24" aria-hidden="true"><path d="M6.6 10.8c1.4 2.8 3.8 5.1 6.6 6.6l2.2-2.2c.3-.3.7-.4 1-.2 1.1.4 2.3.6 3.6.6.6 0 1 .4 1 1V20c0 .6-.4 1-1 1C10.6 21 3 13.4 3 4c0-.6.4-1 1-1h3.5c.6 0 1 .4 1 1 0 1.3.2 2.5.6 3.6.1.3 0 .7-.2 1L6.6 10.8z"/></svg>
        518.677.3941
      </li>
      <li>
        <svg viewBox="0 0 24 24" aria-hidden="true"><path d="M2 5h20v14H2z M4 7v.5l8 5 8-5V7l-8 5z" fill-rule="evenodd"/></svg>
        marissa@calmbriefcounsel.net
      </li>
      <li>
        <span class="handle-mark" aria-hidden="true"></span>
        @calmbriefcounsel
      </li>
    </ul>

    <svg class="footer" viewBox="0 0 1000 60" aria-hidden="true">
      <defs>
        <linearGradient id="band" x1="0" x2="1" y1="0" y2="0">
          <stop offset="0" stop-color="#421121"/>
          <stop offset="1" stop-color="#171B2B"/>
        </linearGradient>
      </defs>
      <rect x="44" y="20" width="510" height="5" fill="#4a4a52"/>
      <polygon points="580,4 1000,4 1000,60 44,60 44,42 556,42" fill="url(#band)"/>
    </svg>
    <span class="site">
      <svg viewBox="0 0 24 24" aria-hidden="true"><circle cx="12" cy="12" r="9.5"/><ellipse cx="12" cy="12" rx="4" ry="9.5"/><path d="M2.5 12h19M4 7h16M4 17h16"/></svg>
      calmbriefcounsel.net
    </span>
  </main>
</body>
</html>
```